harvest Soon Book Cover Design for real estate investment book

I am looking for a Book Cover design for my new book. I would like designs for a hardcover, softcover and Lumora book.

The book deals with real estate and mortgage investments. Looking for a clean, bright simple design. Want to cover to be White with big RED letters. See "Dancing past Noon" book for an example ... see attached.

Target Market(s)

Affluent people with money looking for investment solutions.

Industry/Entity Type

Financial Service

Font styles to use
Serif

Requirements
Must have
• Bright clean design that will be appealing to affluent people.
• Title: harvest SOON
• Subtitle: A quiet method for thriving through land holdings
• subsubtitle: Secrets the Bank Teller Keeps Hidden From Clients...
• Author: Ned Falconby
• My Picture on the inside cover or on the back cover
• Book Description, Author description
Nice to have
• Focus on the Front cover look and feel first. Then we can look at the inside flaps and back cover. I will need to send you text. This is for the full cover. Front. Back. Spine. Inside flaps fro hardcover.

```html
<!DOCTYPE html>
<html lang="en">
<head>
<meta charset="utf-8">
<title>harvest SOON — Book Cover</title>
<link rel="stylesheet" href="https://fonts.googleapis.com/css2?family=Abril+Fatface&family=Roboto+Slab:wght@400;700;800&display=swap">
<style>
  :root {
    --stage: #a9d6d0;
    --paper: #ffffff;
    --red: #d71920;
    --photo-light: #e9ece6;
    --photo-green: #8fae6a;
    --photo-roof: #8a7462;
    --photo-house: #d9582b;
  }
  * { box-sizing: border-box; margin: 0; padding: 0; }
  html, body {
    width: 1200px;
    height: 787px;
    overflow: hidden;
    background: var(--stage);
  }
  .stage {
    width: 1200px;
    height: 787px;
    display: flex;
    align-items: center;
    justify-content: center;
  }
  .cover {
    position: relative;
    width: 500px;
    height: 720px;
    background: var(--paper);
    display: flex;
    flex-direction: column;
    color: var(--red);
    font-family: "Roboto Slab", Georgia, serif;
  }
  .cover__edge {
    height: 16px;
    background: var(--red);
    flex: none;
  }
  .cover__head {
    padding: 26px 28px 18px;
    text-align: center;
  }
  .cover__author {
    font-weight: 700;
    font-size: 20px;
    letter-spacing: 0.28em;
    text-transform: uppercase;
  }
  .cover__title {
    font-family: "Abril Fatface", Georgia, serif;
    font-weight: 400;
    font-size: 74px;
    line-height: 1;
    letter-spacing: 0.02em;
    text-transform: uppercase;
    margin-top: 8px;
  }
  .cover__subtitle {
    font-weight: 700;
    font-size: 17px;
    line-height: 1.3;
    letter-spacing: 0.04em;
    text-transform: uppercase;
    margin-top: 12px;
  }
  .cover__photo {
    flex: 1;
    margin: 0 0;
    background:
      radial-gradient(ellipse 40% 45% at 45% 55%, var(--photo-house) 0%, rgba(217,88,43,0.55) 45%, transparent 75%),
      radial-gradient(ellipse 30% 30% at 55% 35%, var(--photo-roof) 0%, transparent 70%),
      linear-gradient(120deg, var(--photo-light) 0%, var(--photo-green) 55%, var(--photo-light) 100%);
  }
  .cover__foot {
    padding: 22px 28px 26px;
    text-align: center;
  }
  .cover__tagline {
    font-weight: 800;
    font-size: 22px;
    letter-spacing: 0.03em;
    text-transform: uppercase;
  }
  .cover__tagline-sub {
    font-weight: 400;
    font-size: 15px;
    letter-spacing: 0.05em;
    text-transform: uppercase;
    margin-top: 6px;
  }
</style>
</head>
<body>
  <main class="stage">
    <article class="cover">
      <div class="cover__edge"></div>
      <header class="cover__head">
        <p class="cover__author">Ned Falconby</p>
        <h1 class="cover__title">harvest SOON</h1>
        <p class="cover__subtitle">A quiet method for thriving<br>through land holdings</p>
      </header>
      <div class="cover__photo" role="img" aria-label="Photo of a hand dropping a coin into a small red toy house with a shingled roof, garden greenery behind"></div>
      <footer class="cover__foot">
        <p class="cover__tagline">Secrets the Bank Teller</p>
        <p class="cover__tagline-sub">Keeps Hidden From Clients...</p>
      </footer>
      <div class="cover__edge"></div>
    </article>
  </main>
</body>
</html>
```